Wordpress Design Project - QuorvanLabs

I would like our existing old website at www.quorvanlabs.example to be redesigned to a more modern attractive site using Wordpress, a total of 5 web pages. And also installed onto our new web hosting site. Please visit the existing website using Microsoft Internet explorer to see the content.
The new site must be compatible with all popular web browsers and mobile devices (if possible).
There should be a contact button available on each page with an associated form in case an interested person wants to contact us. This form must be spam proof not allowing automated crawlers from activating it.
Updates

There are only 5 pages web pages to this QuorvanLabs project.

Industry/Entity Type

Internet

```html
<!DOCTYPE html>
<html lang="en">
<head>
<meta charset="utf-8">
<title>QuorvanLabs – Telephonic Solutions</title>
<link rel="stylesheet" href="https://fonts.googleapis.com/css2?family=Arimo:ital,wght@0,400;0,700;1,400;1,700&display=swap">
<style>
:root{
  --blue:#1e90d4;
  --blue-dark:#0d7cc0;
  --blue-light:#c9e8f6;
  --band:#2a8ed3;
  --ink:#333;
  --grey:#555;
  --line:#cfcfcf;
  --footer:#242424;
  --white:#fff;
  --navy:#1a3a7a;
}
*{margin:0;padding:0;box-sizing:border-box}
html,body{width:1200px;height:1147px;overflow:hidden}
body{position:relative;background:var(--white);font-family:"Arimo",Arial,sans-serif;color:var(--ink)}
.abs{position:absolute}

.top-strip{left:0;top:0;width:1200px;height:8px;background:var(--blue-dark)}
.header{left:0;top:8px;width:1200px;height:93px;background:linear-gradient(90deg,#d9eff8 0%,#bfe3f4 45%,#a9d9ef 65%,#d5eef8 100%)}
.brand{left:247px;top:26px;display:flex;align-items:center;gap:12px}
.brand-mark{width:40px;height:40px;border-radius:50%;background:var(--navy)}
.brand-name{font-size:26px;font-weight:700;color:var(--navy)}
.brand-tag{left:350px;top:62px;font-size:7px;color:var(--navy)}
.search{left:746px;top:41px;width:188px;height:16px;background:#fff;border:1px solid #aac8d8}
.search-icon{left:940px;top:43px}

.hero{left:0;top:101px;width:1200px;height:233px;background:linear-gradient(100deg,#fff 0%,#fff 45%,#e3f3fa 65%,#cde9f6 80%,#fff 100%)}
.hero-photo{left:244px;top:118px;width:312px;height:186px;border-radius:14px;background:linear-gradient(160deg,#7d8186,#3f4347 60%,#26292c)}
.hero-title{left:583px;top:129px;font-size:32px;font-weight:700;color:#4a4a4a;line-height:37px}
.hero-title .accent{color:var(--blue);font-size:38px}
.hero-copy{left:583px;top:243px;font-size:9px;line-height:15px;color:#555}
.arrow{top:198px}
.arrow-left{left:238px}
.arrow-right{left:950px}

.nav{left:0;top:334px;width:1200px;height:66px;background:linear-gradient(#33a6e0,#1690d1 55%,#0f83c5);box-shadow:0 6px 10px rgba(0,0,0,.12)}
.nav-list{left:300px;top:334px;height:66px;display:flex;list-style:none}
.nav-list li{height:66px;display:flex;align-items:center;padding:0 18px;font-size:12px;color:#fff;border-left:1px solid rgba(255,255,255,.25);border-right:1px solid rgba(0,60,110,.25)}
.nav-list li.active{background:rgba(255,255,255,.12);font-weight:700}

.welcome-title{left:275px;top:446px;font-size:21px;color:var(--blue)}
.welcome-title strong{font-style:italic}
.welcome-lead{left:275px;top:487px;font-size:8px;font-weight:700;color:#333}
.welcome-copy{left:275px;top:516px;width:540px;font-size:8px;line-height:15px;color:#444}
.welcome-copy a{color:var(--blue)}
.welcome-illustration{left:846px;top:480px;width:60px;height:74px;background:linear-gradient(#f4f6f8,#d8dde2);border:1px solid #c9cfd5}
.divider{left:245px;top:579px;width:708px;height:1px;background:var(--line)}

.col-title{font-size:20px;color:var(--blue);top:608px}
.offer-title{left:277px}
.services-title{left:642px}
.col-rule{left:616px;top:612px;width:1px;height:192px;background:var(--line)}
.offer-icon{width:48px;height:44px;background:linear-gradient(#eef1f4,#c5ccd3)}
.offer-icon.doc{left:270px;top:663px}
.offer-icon.screen{left:272px;top:744px;background:linear-gradient(#5aa3e8,#1c5fb3)}
.offer-item{left:335px;font-size:8px;line-height:15px;color:#444}
.offer-item h3{font-size:8px;color:var(--blue);font-weight:700}
.offer-1{top:655px}
.offer-2{top:745px}

.services{left:642px;top:654px;list-style:none;width:292px}
.services li{height:21px;display:flex;align-items:center;gap:13px;font-size:9.5px;color:#444}
.services li span{border-bottom:1px solid var(--line);padding-bottom:2px}
.services .bullet{width:7px;height:7px;border-radius:50%;border:1px solid #999;flex:none;border-bottom:1px solid #999;padding:0}

.band{left:0;top:835px;width:1200px;height:228px;background:linear-gradient(#2a8ed3,#2e97d9)}
.band-rule{top:852px;width:1px;height:190px;background:rgba(255,255,255,.25)}
.band-title{top:862px;font-size:17px;color:#fff}
.band-text{font-size:8px;line-height:15px;color:#fff}
.testimonial{left:265px;top:905px;width:180px;font-style:italic}
.testimonial-name{left:382px;top:1001px;font-weight:700;font-size:8.5px}
.news{left:512px;top:905px;width:190px}
.contact{left:756px;top:906px;width:175px;line-height:13.5px}
.contact a{color:#fff}
.follow{left:826px;top:1036px;font-size:6px;color:#fff;letter-spacing:2px}
.follow-dot{left:900px;top:1032px;width:28px;height:28px;border-radius:50%;background:#5cb6ea}

.footer{left:0;top:1063px;width:1200px;height:84px;background:var(--footer)}
.footer-links{left:270px;top:1098px;display:flex;list-style:none}
.footer-links li{font-size:8px;color:#fff;padding:0 20px;border-left:1px solid #555;height:12px;line-height:12px}
.footer-links li:first-child{padding-left:0;border-left:0}
.copyright{left:729px;top:1104px;font-size:8px;color:#fff}
</style>
</head>
<body>
<div class="abs top-strip"></div>
<header class="abs header"></header>
<div class="abs brand"><span class="brand-mark"></span><span class="brand-name">QuorvanLabs</span></div>
<div class="abs brand-tag">A Leading Edge Technology Company</div>
<div class="abs search"></div>
<svg class="abs search-icon" width="12" height="12" viewBox="0 0 12 12"><circle cx="4.5" cy="4.5" r="3" fill="none" stroke="#555" stroke-width="1.4"/><line x1="7" y1="7" x2="11" y2="11" stroke="#555" stroke-width="1.6"/></svg>

<section class="abs hero"></section>
<div class="abs hero-photo" role="img" aria-label="Photo of a grey office desk IP telephone with display and keypad"></div>
<h1 class="abs hero-title">Telephonic Solutions<br>to improve your<br><span class="accent">business!</span></h1>
<p class="abs hero-copy">Been the industry's standard dummy text ever since thes. Simply dummy text orem<br>Ipsum has&nbsp; standard dummy tex. Undustry's standard.<br>Dummy text ever since thes.</p>
<svg class="abs arrow arrow-left" width="32" height="32" viewBox="0 0 32 32"><path d="M3 16 L16 3 V10 H29 V22 H16 V29 Z" fill="#7ccff0" stroke="#3aa6dc" stroke-width="1.5"/></svg>
<svg class="abs arrow arrow-right" width="32" height="32" viewBox="0 0 32 32"><path d="M29 16 L16 3 V10 H3 V22 H16 V29 Z" fill="#7ccff0" stroke="#3aa6dc" stroke-width="1.5"/></svg>

<nav class="abs nav"></nav>
<ul class="abs nav-list">
  <li class="active">HOME</li>
  <li style="padding:0 22px 0 34px">TELEPHONE VOIP SOLUTION</li>
  <li style="padding:0 16px 0 24px">IP, LAN AND INTERNET</li>
  <li style="padding:0 20px 0 34px">SUPPORT SERVICES</li>
  <li style="padding:0 28px 0 27px">CONTACTS</li>
</ul>

<h2 class="abs welcome-title">Welcome to <strong>QuorvanLabs</strong></h2>
<p class="abs welcome-lead">Simply dummy text of the printing and typesetting industry.</p>
<p class="abs welcome-copy">Lorem Ipsum has been the industry's standard dummy text ever since thes, when an unknown printer.Simply dummy text of the printing and typesetting industry. Lorem Ipsum has been the <a href="#">ustry's standard dummy text</a> ever since thes, when an unknown printer.Simply dummy text of the printing and typesetting industry.</p>
<div class="abs welcome-illustration" role="img" aria-label="Illustration of a paper sheet with a pencil"></div>
<div class="abs divider"></div>

<h2 class="abs col-title offer-title">What&nbsp; we offer</h2>
<div class="abs offer-icon doc" role="img" aria-label="Illustration of stacked documents"></div>
<div class="abs offer-item offer-1"><h3>Has been the industry's standard dummy.</h3><p>Simply dummy text of the printing and typesetting industry.<br>Lorem Ipsum has been the industry's standard dummy text ever since<br>thes, when an unknown printer.</p></div>
<div class="abs offer-icon screen" role="img" aria-label="Illustration of a computer monitor"></div>
<div class="abs offer-item offer-2"><h3>Simply dummy text of the printing and typesetting industry.</h3><p>&nbsp;Lorem Ipsum has been the industry's standard dummy text.<br>Ever since thes, when an unknown printer.</p></div>
<div class="abs col-rule"></div>

<h2 class="abs col-title services-title">Our services</h2>
<ul class="abs services">
  <li><i class="bullet"></i><span>Simply dummy text of the printing and typesetting industry.</span></li>
  <li><i class="bullet"></i><span>Lorem has been the industry's standard dummy text.</span></li>
  <li><i class="bullet"></i><span>Ever since thes, <small style="font-size:7.5px">when an unknown printer.</small></span></li>
  <li><i class="bullet"></i><span>Has been the industry's standard dummy text ever since thes.</span></li>
  <li><i class="bullet"></i><span>Simply dummy text of the printing and typesetting industry.</span></li>
  <li><i class="bullet"></i><span>Lorem Ipsum has been the industry's standard dummy text.</span></li>
  <li><i class="bullet"></i><span style="border:0">Ever since thes when an unknown printer.</span></li>
</ul>

<section class="abs band"></section>
<div class="abs band-rule" style="left:476px"></div>
<div class="abs band-rule" style="left:724px"></div>
<h2 class="abs band-title" style="left:263px">Testimonials</h2>
<h2 class="abs band-title" style="left:508px">News &amp;&nbsp; Events</h2>
<h2 class="abs band-title" style="left:752px">Contact us</h2>
<p class="abs band-text testimonial">"Lorem Ipsum is simply dummy text of the printing and typesetting industry. Lorem Ips has been the. industry's" standard&nbsp; text ever since the 1500s, when an unknown printer dummy..."</p>
<p class="abs band-text testimonial-name" style="color:#fff">Emrel Vostan</p>
<div class="abs band-text news"><p><b>12th/ april/ 2010</b><br>Has been the industry's standard dummy text ever since thes.</p><br><p><b>13th/ april/ 2010</b><br>Simply dummy text of the printing and typesetting industry.</p></div>
<p class="abs band-text contact">Feel free to contact me or up below in the following. I will be in touch shortly.<br>Address: 415 Larkfield Road, Unit 12<br>Ashvale, Northshire K2M 4T9<br>Telephone: +100-2040-3060<br>FAX: +402-7719<br>Others: +305 - 0441 - 02276<br>E-mail: <a href="#">info@quorvanlabs.example</a></p>
<span class="abs follow">FOLLOW ME</span>
<span class="abs follow-dot"></span>

<footer class="abs footer"></footer>
<ul class="abs footer-links"><li>home</li><li>about</li><li>contact</li><li>rss feed</li></ul>
<p class="abs copyright">© Copyright 2013. quorvanlabs.example. All Rights Reserved</p>
</body>
</html>
```